Brightwell Power Solutions

We'd like a web design that's beautiful and professional. We replace existing inefficient systems (mostly lighting at the moment but expanding) with highly efficient systems.

```html
<!DOCTYPE html>
<html lang="en">
<head>
<meta charset="utf-8">
<title>Brightwell Power Solutions</title>
<link href="https://fonts.googleapis.com/css2?family=Questrial&family=Open+Sans:wght@400;600;700&display=swap" rel="stylesheet">
<style>
  :root {
    --brand-green: #5a8a16;
    --brand-green-dark: #3f6a0c;
    --hero-deep: #1f3a08;
    --hero-mid: #3f7512;
    --hero-glow: #b9e05a;
    --headline: #d6ec7a;
    --nav-bg: #d7d7d5;
    --nav-text: #4a4a48;
    --paper: #efece4;
    --paper-line: #d9d4c8;
    --ink: #333330;
    --ink-soft: #6b6a64;
    --footer: #262624;
    --footer-text: #d9d9d4;
    --white: #ffffff;
  }
  * { box-sizing: border-box; margin: 0; padding: 0; }
  html, body { width: 1200px; height: 852px; overflow: hidden; background: var(--white); }
  body { font-family: "Open Sans", Arial, sans-serif; color: var(--ink); }
  .page { position: relative; width: 1200px; height: 852px; background: var(--paper); }

  /* Header */
  .site-header { position: absolute; top: 0; left: 0; width: 100%; height: 44px; background: var(--nav-bg); }
  .brand { position: absolute; top: 6px; left: 24px; z-index: 3; width: 250px; height: 96px; background: var(--white);
           display: flex; align-items: center; gap: 12px; padding: 0 16px; box-shadow: 0 2px 6px rgba(0,0,0,.25); }
  .brand-mark { width: 22px; height: 22px; background: var(--brand-green); flex: none; }
  .brand-name { font-family: "Questrial", Arial, sans-serif; font-size: 21px; line-height: 1.15; color: var(--brand-green); }
  .main-nav { position: absolute; right: 24px; top: 0; height: 44px; display: flex; }
  .main-nav a { display: flex; align-items: center; padding: 0 20px; font-size: 13px; font-weight: 600;
                color: var(--nav-text); text-decoration: none; }
  .main-nav a.is-active { background: var(--brand-green); color: var(--white); }

  /* Hero */
  .hero { position: absolute; top: 44px; left: 0; width: 100%; height: 356px;
          background: radial-gradient(ellipse 38% 60% at 58% 62%, var(--hero-glow) 0%, var(--hero-mid) 45%, var(--hero-deep) 100%); }
  .hero-headline { position: absolute; right: 40px; top: 170px; text-align: right;
                   font-family: "Questrial", Arial, sans-serif; font-size: 34px; line-height: 1.22;
                   letter-spacing: 1px; color: var(--headline); text-transform: uppercase; }

  /* Who we are */
  .intro { position: absolute; top: 400px; left: 0; width: 100%; height: 118px; padding: 14px 40px;
           border-bottom: 1px solid var(--paper-line); }
  .intro h2 { font-family: "Questrial", Arial, sans-serif; font-weight: 400; font-size: 30px; color: var(--ink); }
  .intro p { margin-top: 8px; width: 820px; font-size: 12px; line-height: 1.6; color: var(--ink-soft); }
  .intro-photo { position: absolute; right: 40px; top: 14px; width: 170px; height: 66px; border-radius: 4px;
                 background: linear-gradient(135deg, #5c5850, #b8a999 60%, #e6ddd1); }
  .intro-button { position: absolute; right: 40px; top: 84px; width: 170px; height: 24px; background: #cfcac0;
                  font-size: 12px; font-weight: 700; display: flex; align-items: center; justify-content: center; color: var(--ink); }

  /* Features */
  .features { position: absolute; top: 522px; left: 40px; right: 40px; height: 100px; display: flex; gap: 24px; }
  .feature { flex: 1; text-align: center; padding-top: 6px; border-bottom: 3px solid var(--paper-line); }
  .feature h3 { font-size: 12px; font-weight: 600; margin-bottom: 6px; }
  .feature svg { display: block; margin: 0 auto 6px; }
  .feature p { font-size: 10.5px; line-height: 1.45; color: var(--ink-soft); }

  /* Events & gallery */
  .columns { position: absolute; top: 628px; left: 40px; right: 40px; height: 128px; display: flex; gap: 28px; }
  .col-title { font-size: 12px; font-weight: 700; border-bottom: 3px solid var(--paper-line); padding-bottom: 3px; margin-bottom: 8px; }
  .events { flex: 1; }
  .event { display: flex; gap: 14px; }
  .event-photo { width: 130px; height: 72px; flex: none; background: linear-gradient(160deg, #e3a63a, #b8651c 55%, #6c4a1e); }
  .event h4 { font-size: 12px; font-weight: 700; margin-bottom: 3px; }
  .event p { font-size: 10.5px; line-height: 1.45; color: var(--ink-soft); }
  .read-more { display: inline-block; margin-top: 4px; float: right; background: var(--brand-green); color: var(--white);
               font-size: 11px; font-weight: 600; padding: 2px 12px; }
  .event-meta { display: flex; gap: 4px; margin-top: 6px; }
  .event-meta span { flex: 1; background: var(--brand-green-dark); color: var(--white); font-size: 10px; text-align: center; padding: 2px 0; }
  .gallery { flex: 1; }
  .gallery-grid { display: grid; grid-template-columns: 1fr 1fr; gap: 6px; }
  .gallery-grid div { height: 44px; }
  .g1 { background: linear-gradient(135deg, #8a7a52, #c7b98a); }
  .g2 { background: linear-gradient(135deg, #3f6a2a, #9db86a); }
  .g3 { background: linear-gradient(135deg, #a0845a, #d8c39c); }
  .g4 { background: linear-gradient(135deg, #8a8a86, #b83020 70%, #d8d6d0); }

  /* Footer */
  .site-footer { position: absolute; top: 762px; left: 0; width: 100%; height: 90px; background: var(--footer);
                 color: var(--footer-text); padding: 10px 40px; display: flex; gap: 28px; }
  .site-footer h3 { font-size: 12px; font-weight: 700; color: var(--white); margin-bottom: 6px; }
  .newsletter { flex: 1; }
  .newsletter p { font-size: 10.5px; line-height: 1.45; }
  .signup { display: flex; margin-top: 8px; }
  .signup span { flex: 1; background: var(--white); color: #888; font-size: 10px; padding: 3px 6px; }
  .signup b { background: var(--brand-green); color: var(--white); font-size: 10px; padding: 3px 10px; }
  .featured { flex: 1; }
  .featured-photo { height: 52px; background: linear-gradient(180deg, #a9c8df, #e6eef2 60%, #c9d6a8); }
</style>
</head>
<body>
<div class="page">
  <header class="site-header">
    <div class="brand">
      <span class="brand-mark"></span>
      <span class="brand-name">Brightwell Power Solutions</span>
    </div>
    <nav class="main-nav">
      <a class="is-active" href="#">Home</a>
      <a href="#">Why</a>
      <a href="#">LED?</a>
      <a href="#">Case Studies</a>
      <a href="#">FAQ</a>
      <a href="#">Energy Audit</a>
    </nav>
  </header>

  <section class="hero" role="img" aria-label="Row of hanging light bulbs with one glowing LED bulb on a green background">
    <p class="hero-headline">Request<br>a no<br>obligation<br>free audit</p>
  </section>

  <section class="intro">
    <h2>Who We Are</h2>
    <p>Brightwell Power Solutions is an independent energy partner that replaces outdated lighting and power systems with efficient ones. Our certified team audits your site, plans the upgrade and handles installation so your savings start sooner and last longer.</p>
    <div class="intro-photo" role="img" aria-label="Photo of an energy advisor with a client"></div>
    <div class="intro-button">Request Audit</div>
  </section>

  <section class="features">
    <div class="feature">
      <h3>Who we are</h3>
      <svg width="30" height="24" viewBox="0 0 30 24" aria-hidden="true"><g fill="#333330"><circle cx="9" cy="5" r="4"/><circle cx="21" cy="5" r="4"/><rect x="4" y="11" width="10" height="13" rx="3"/><rect x="16" y="11" width="10" height="13" rx="3"/></g></svg>
      <p>A local team focused on cutting energy costs.</p>
    </div>
    <div class="feature">
      <h3>What we do</h3>
      <svg width="24" height="24" viewBox="0 0 24 24" aria-hidden="true"><circle cx="12" cy="12" r="8" fill="none" stroke="#333330" stroke-width="4" stroke-dasharray="4 2.3"/><circle cx="12" cy="12" r="3" fill="#333330"/></svg>
      <p>Audits, design and installation of efficient lighting.</p>
    </div>
    <div class="feature">
      <h3>Save environment</h3>
      <svg width="24" height="24" viewBox="0 0 24 24" aria-hidden="true"><path d="M4 20 C4 8 12 3 21 3 C21 13 15 20 4 20 Z" fill="#333330"/><path d="M4 20 L14 10" stroke="#efece4" stroke-width="1.5"/></svg>
      <p>Lower usage means fewer emissions every single day.</p>
    </div>
    <div class="feature">
      <h3>Reuse your trash</h3>
      <svg width="24" height="24" viewBox="0 0 24 24" aria-hidden="true"><rect x="5" y="4" width="14" height="3" fill="#333330"/><path d="M6 8 H18 L17 22 H7 Z" fill="#333330"/></svg>
      <p>Old fixtures are collected and recycled responsibly.</p>
    </div>
  </section>

  <section class="columns">
    <div class="events">
      <div class="col-title">Events</div>
      <div class="event">
        <div class="event-photo" role="img" aria-label="Autumn park path with golden trees"></div>
        <div>
          <h4>Green Day Event</h4>
          <p>Join us for a morning of free site tours, efficiency tips and product demos.</p>
          <span class="read-more">Read More</span>
        </div>
      </div>
      <div class="event-meta"><span>24 Mar</span><span>09:00 AM</span><span>Venue</span></div>
    </div>
    <div class="gallery">
      <div class="col-title">Image Gallery</div>
      <div class="gallery-grid">
        <div class="g1" role="img" aria-label="Gallery photo of a field"></div>
        <div class="g2" role="img" aria-label="Gallery photo of a forest"></div>
        <div class="g3" role="img" aria-label="Gallery photo of wood and nature"></div>
        <div class="g4" role="img" aria-label="Gallery photo of a red flower"></div>
      </div>
    </div>
  </section>

  <footer class="site-footer">
    <div class="newsletter">
      <h3>Newsletter</h3>
      <p>Sign up for seasonal updates on rebates, new fixtures and upcoming events.</p>
      <div class="signup"><span>Your email address</span><b>Go</b></div>
    </div>
    <div class="featured">
      <h3>Featured Stuff</h3>
      <div class="featured-photo" role="img" aria-label="Photo of blue sky over a meadow"></div>
    </div>
  </footer>
</div>
</body>
</html>
```